Outdoor Property Monument Sign

I am looking for an outdoor monument sign for an apartment complex in Newark, DE, USA. The property website is www.brightmeadowlofts.com. There you can see photos in the photo gallery of the apartment complex as well as the interior apartments. We rent primarily to college student, but we want the monument sign to fit with our aesthetic and look classy. We would want some illumination incorporated in the sign, and we do have electric run to the area the sign will be. I have attached a google earth image of the property as well, with a RED X where the sign will go.
The property address is 847 Fenwick Ln, Newark, DE 19713.

There are actually two locations where we need a sign, as we have two entrances. The focus should be on the larger monument sign, but if you want to include a smaller monument sign that has a similar look but more simple for the other entry that would be great. The other sign would go where the LIGHT BLUE X is on the google image.

Industry/Entity Type

Off-Campus Student Housing

Font styles to use
Sans Serif

Requirements
Must have
• THE COPPER BEND, A Lakeshore Crest Residence, and the logo

```html
<!DOCTYPE html>
<html lang="en">
<head>
<meta charset="utf-8">
<title>The Copper Bend Monument Sign</title>
<link rel="stylesheet" href="https://fonts.googleapis.com/css2?family=Anton&family=Montserrat:wght@800&display=swap">
<style>
  :root {
    --backdrop: #6b6b6b;
    --sign-white: #ffffff;
    --brand-blue: #00489a;
    --brand-yellow: #f7cf00;
    --ink-black: #000000;
  }
  html, body {
    margin: 0;
    padding: 0;
    width: 1200px;
    height: 2267px;
    overflow: hidden;
    background: var(--backdrop);
  }
  .canvas {
    position: relative;
    width: 1200px;
    height: 2267px;
  }
  .sign {
    position: absolute;
    left: 128px;
    top: 1195px;
    width: 945px;
    height: 946px;
    display: flex;
    flex-direction: column;
  }
  .sign-brand {
    height: 432px;
    background: var(--sign-white);
    display: flex;
    flex-direction: column;
    align-items: center;
    justify-content: center;
    gap: 40px;
  }
  .brand-mark {
    display: block;
  }
  .brand-name {
    font-family: "Montserrat", sans-serif;
    font-weight: 800;
    font-size: 54px;
    color: var(--brand-blue);
    letter-spacing: 1px;
    line-height: 1;
  }
  .sign-title {
    height: 352px;
    background: var(--brand-blue);
    color: var(--sign-white);
    font-family: "Montserrat", sans-serif;
    font-weight: 800;
    text-align: center;
    display: flex;
    flex-direction: column;
    align-items: center;
    justify-content: center;
    margin: 0;
  }
  .title-lead {
    font-size: 160px;
    line-height: 0.9;
    letter-spacing: -2px;
  }
  .title-main {
    font-size: 124px;
    line-height: 1.05;
    letter-spacing: -3px;
    white-space: nowrap;
  }
  .sign-tagline {
    flex: 1;
    background: var(--brand-yellow);
    color: var(--ink-black);
    font-family: "Anton", sans-serif;
    font-size: 70px;
    text-transform: uppercase;
    display: flex;
    align-items: center;
    justify-content: center;
    white-space: nowrap;
    margin: 0;
  }
</style>
</head>
<body>
  <main class="canvas">
    <section class="sign">
      <div class="sign-brand">
        <svg class="brand-mark" width="220" height="220" viewBox="0 0 220 220" aria-hidden="true">
          <circle cx="110" cy="110" r="110" fill="var(--brand-blue)"/>
        </svg>
        <span class="brand-name">Meadowgate Homes</span>
      </div>
      <h1 class="sign-title">
        <span class="title-lead">THE</span>
        <span class="title-main">COPPER BEND</span>
      </h1>
      <p class="sign-tagline">A Lakeshore Crest Residence</p>
    </section>
  </main>
</body>
</html>
```